Marrowby Nature Alliance needs a fundraiser poster

We are having an annual awards night and fundraiser.

On the top of the poster please put "Marrowby Nature Alliance Annual Awards Night and Fundraiser"

Date: March 25, 2023
Time: 6:00pm doors open. Supper at 7:00pm
Location: Quenford Sportsdome Auditorium
Cost: $40 for Adults, $20 for 18 and under

We also would like on the poster, "Live Auctions, Silent auctions, and raffles"
"Serving Elk, Moose, and Wild Boar. Also beef"

```html
<!DOCTYPE html>
<html lang="en">
<head>
<meta charset="utf-8">
<title>Marrowby Nature Alliance Annual Awards Night and Fundraiser</title>
<link rel="stylesheet" href="https://fonts.googleapis.com/css2?family=Cinzel:wght@600;700;800&family=Oswald:wght@300;400;500&family=Poppins:wght@300;400;600&display=swap">
<style>
  :root {
    --ink: #050505;
    --snow: #ebebeb;
    --snow-light: #f3f3f3;
    --stone: #6a6a6a;
    --tag: #d3d3d3;
    --gold: #f4a51c;
    --pin: #e0192b;
    --white: #ffffff;
  }
  * { box-sizing: border-box; margin: 0; padding: 0; }
  html, body { width: 750px; height: 1200px; overflow: hidden; background: var(--snow); }
  .poster {
    position: relative;
    width: 750px; height: 1200px;
    background: radial-gradient(ellipse at 50% 70%, var(--snow-light), var(--snow) 70%);
    overflow: hidden;
    font-family: "Poppins", sans-serif;
    color: var(--ink);
  }
  .night-sky {
    position: absolute; left: 0; top: 0; width: 750px; height: 300px;
    background: var(--ink);
  }
  .forest-line {
    position: absolute; left: 0; top: 215px; width: 750px; height: 200px;
    background: linear-gradient(to bottom, var(--ink) 0%, #3a3a3a 35%, #cfcfcf 75%, var(--snow) 100%);
  }
  .brand {
    position: absolute; left: 0; top: 92px; width: 750px;
    text-align: center; color: var(--white);
    font-family: "Cinzel", serif; font-weight: 700;
  }
  .brand-name { display: block; font-size: 34px; letter-spacing: 2px; line-height: 1; }
  .brand-sub { display: block; font-size: 13px; letter-spacing: 3px; margin-top: 8px; }
  .headline {
    position: absolute; left: 0; top: 430px; width: 750px;
    text-align: center; font-family: "Cinzel", serif; font-weight: 800; line-height: 1;
  }
  .headline-annual { display: block; font-size: 96px; letter-spacing: 2px; }
  .headline-awards { display: block; font-size: 50px; color: var(--stone); margin-top: 4px; letter-spacing: 1px; }
  .headline-fund { display: block; font-size: 52px; margin-top: 2px; letter-spacing: 1px; }
  .date-card {
    position: absolute; left: 300px; top: 664px; width: 152px; height: 202px;
    border: 2px solid #b5b5b5; text-align: center;
    font-family: "Cinzel", serif; font-weight: 700;
  }
  .date-month { display: block; font-size: 34px; margin-top: 6px; line-height: 1; }
  .date-day { display: block; font-size: 100px; color: var(--stone); line-height: 0.9; font-family: "Poppins", sans-serif; font-weight: 600; letter-spacing: -2px; }
  .date-year {
    position: absolute; left: 7px; right: 7px; bottom: 7px; height: 50px;
    background: var(--ink); color: var(--gold);
    font-family: "Oswald", sans-serif; font-weight: 300; font-size: 34px;
    letter-spacing: 14px; text-indent: 14px; line-height: 50px;
  }
  .schedule {
    position: absolute; left: 0; top: 900px; width: 750px; text-align: center;
    font-family: "Oswald", sans-serif; font-weight: 300; font-size: 28px; letter-spacing: 1px;
  }
  .schedule b { font-weight: 500; }
  .schedule .divider { display: inline-block; width: 1px; height: 30px; background: #999; vertical-align: middle; margin: 0 14px; }
  .venue {
    position: absolute; left: 0; top: 938px; width: 750px; text-align: center;
    font-weight: 600; font-size: 20px;
  }
  .venue svg { width: 13px; height: 17px; vertical-align: -1px; margin-right: 3px; }
  .activities {
    position: absolute; left: 0; top: 970px; width: 750px; text-align: center;
    font-weight: 300; font-size: 19px;
  }
  .activities .sep { margin: 0 8px; }
  .menu {
    position: absolute; left: 203px; top: 1030px; width: 341px; height: 30px;
    display: flex; gap: 4px;
  }
  .menu-item {
    flex: 1; background: var(--tag); text-align: center;
    font-family: "Oswald", sans-serif; font-weight: 300; font-size: 19px; line-height: 30px; letter-spacing: -0.5px;
  }
  .tickets {
    position: absolute; left: 203px; top: 1072px; width: 341px; height: 58px;
    display: flex; gap: 6px;
  }
  .ticket { flex: 1; display: flex; background: var(--tag); }
  .ticket-price {
    width: 68px; background: var(--ink); color: var(--gold);
    font-family: "Oswald", sans-serif; font-weight: 400; font-size: 42px; line-height: 58px; text-align: center;
  }
  .ticket-price sup { font-size: 20px; vertical-align: 16px; }
  .ticket-label {
    padding-left: 6px; display: flex; flex-direction: column; justify-content: center;
    font-weight: 600; font-size: 18px; line-height: 1;
  }
</style>
</head>
<body>
<main class="poster">
  <div class="night-sky"></div>
  <div class="forest-line" role="img" aria-label="White pine forest silhouette along the horizon"></div>

  <header class="brand">
    <span class="brand-name">MARROWBY</span>
    <span class="brand-sub">NATURE ALLIANCE</span>
  </header>

  <h1 class="headline">
    <span class="headline-annual">ANNUAL</span>
    <span class="headline-awards">AWARDS NIGHT &amp;</span>
    <span class="headline-fund">FUNDRAISER</span>
  </h1>

  <div class="date-card">
    <span class="date-month">MARCH</span>
    <span class="date-day">25</span>
    <span class="date-year">2023</span>
  </div>

  <p class="schedule"><b>6:00PM</b> DOORS OPEN<span class="divider"></span>SUPPER AT <b>7:00PM</b></p>

  <p class="venue"><svg viewBox="0 0 12 16" aria-hidden="true"><path d="M6 0C2.7 0 0 2.6 0 5.9 0 10.3 6 16 6 16s6-5.7 6-10.1C12 2.6 9.3 0 6 0zm0 8.3A2.4 2.4 0 1 1 6 3.5a2.4 2.4 0 0 1 0 4.8z" fill="var(--pin)"/></svg>Quenford Sportsdome Auditorium</p>

  <p class="activities">Live Auctions<span class="sep">|</span>Silent auctions<span class="sep">|</span>&amp; raffles</p>

  <ul class="menu">
    <li class="menu-item" style="list-style:none">SERVING ELK</li>
    <li class="menu-item" style="list-style:none">MOOSE</li>
    <li class="menu-item" style="list-style:none">WILD BOAR</li>
    <li class="menu-item" style="list-style:none">ALSO BEEF</li>
  </ul>

  <div class="tickets">
    <div class="ticket">
      <span class="ticket-price"><sup>$</sup>40</span>
      <span class="ticket-label">FOR<br>ADULTS</span>
    </div>
    <div class="ticket">
      <span class="ticket-price"><sup>$</sup>20</span>
      <span class="ticket-label">FOR 18<br>&amp; UNDER</span>
    </div>
  </div>
</main>
</body>
</html>
```